Interior Design business card design

I am an interior decorator - dont want to specify decorating more just design.
Want organic looking logo - charcoal and white - with touch of lime green.
Like the idea of some sort of spiral in corner but writing in a line
want lower case, carlamintowe as one and designs in different font underneath. Maybe using c and m as logo.
More modern than traditional. My clients are mid to top end residential

Target Market(s)

medium to top end homeowners

Industry/Entity Type

Residential

Contact Information for Business Card

Carla Mintowe Designs
58 Fallowmere ave
Tindarra 2188 NSW
Tel 0417869214
carlamintowe@quellnet.com.au

Logo Text

Carla Mintowe Designs

Logo styles of interest
Abstract Logo
Lettermark Logo
Requirements
Must have
• Name address ph and e mail
Nice to have
• Contemporary
smart but organic
Should not have
• no traditional fonts

```html
<!DOCTYPE html>
<html lang="en">
<head>
<meta charset="utf-8">
<title>Carla Mintowe Designs – Business Card</title>
<link href="https://fonts.googleapis.com/css2?family=Questrial&display=swap" rel="stylesheet">
<style>
  :root {
    --backdrop: #ecebe7;
    --card-charcoal: #959595;
    --card-white: #f7f7f7;
    --ink-white: #ffffff;
    --ink-charcoal: #6a6a6a;
    --ink-soft: #8a8a8a;
    --mark-faint: #a3a3a3;
    --lime: #7cc242;
    --shadow: rgba(0, 0, 0, 0.18);
  }
  * { margin: 0; padding: 0; box-sizing: border-box; }
  html, body {
    width: 1200px;
    height: 800px;
    overflow: hidden;
    background: var(--backdrop);
    font-family: "Questrial", "Century Gothic", sans-serif;
  }
  .canvas {
    position: relative;
    width: 1200px;
    height: 800px;
  }
  .card {
    position: absolute;
    box-shadow: 0 6px 18px var(--shadow);
  }
  .card-front {
    left: 168px;
    top: 250px;
    width: 560px;
    height: 290px;
    background: var(--card-charcoal);
    overflow: hidden;
  }
  .card-front .monogram-block {
    position: absolute;
    left: 350px;
    top: 30px;
    width: 210px;
    height: 210px;
    background: var(--mark-faint);
  }
  .card-front .wordmark {
    position: absolute;
    left: 44px;
    top: 112px;
    font-size: 21px;
    letter-spacing: 0.3px;
    color: var(--ink-white);
  }
  .card-back {
    left: 470px;
    top: 440px;
    width: 600px;
    height: 250px;
    background: var(--card-white);
  }
  .card-back .brand {
    position: absolute;
    right: 56px;
    top: 46px;
    display: flex;
    align-items: center;
    gap: 12px;
  }
  .card-back .brand-name {
    font-size: 18px;
    letter-spacing: 0.5px;
    color: var(--ink-charcoal);
  }
  .card-back .brand-square {
    width: 34px;
    height: 34px;
    background: var(--ink-charcoal);
  }
  .card-back .contact {
    position: absolute;
    left: 56px;
    bottom: 32px;
    font-size: 12.5px;
    color: var(--ink-soft);
    line-height: 1.55;
  }
  .contact-row {
    display: flex;
    align-items: center;
    gap: 26px;
  }
  .contact-item {
    display: flex;
    align-items: center;
    gap: 6px;
  }
  .contact-icon { width: 12px; height: 12px; display: block; }
</style>
</head>
<body>
  <main class="canvas">
    <section class="card card-front" aria-label="Business card front">
      <div class="monogram-block"></div>
      <p class="wordmark">carlamintowe</p>
    </section>

    <section class="card card-back" aria-label="Business card back">
      <div class="brand">
        <span class="brand-name">carlamintowe designs</span>
        <span class="brand-square"></span>
      </div>
      <div class="contact">
        <p class="address">58 Fallowmere ave Tindarra 2188 NSW</p>
        <div class="contact-row">
          <span class="contact-item">
            <svg class="contact-icon" viewBox="0 0 12 12" aria-hidden="true">
              <circle cx="6" cy="6" r="6" fill="var(--lime)"/>
              <path d="M4 3.2 L5 3 L5.6 4.6 L4.9 5.2 Q5.6 6.6 6.8 7.1 L7.4 6.4 L9 7 L8.8 8 Q8 8.9 6.6 8.3 Q4.2 7.2 3.3 4.8 Q3.1 3.7 4 3.2 Z" fill="#fff"/>
            </svg>
            0417869214
          </span>
          <span class="contact-item">
            <svg class="contact-icon" viewBox="0 0 12 12" aria-hidden="true">
              <circle cx="6" cy="6" r="6" fill="var(--lime)"/>
              <rect x="3" y="4" width="6" height="4.2" fill="none" stroke="#fff" stroke-width="0.9"/>
              <path d="M3 4 L6 6.4 L9 4" fill="none" stroke="#fff" stroke-width="0.9"/>
            </svg>
            carlamintowe@quellnet.com.au
          </span>
        </div>
      </div>
    </section>
  </main>
</body>
</html>
```